Poster Design Project- New Years Eve

We are a fun and quirky bar in St Kilda (www.quillhouse.com.au). We need a poster designed for our New Years Eve Event- details as follows
Project: A1 poster-NYE
Name of Event: Copper Moons
Date of Event: New Years Eve: 31.12.12
Tagline: ‘What happens at Quill stays at Quill’
Time: 8pm-3am
Cost:
$105 all inclusive
-Includes a cocktail on arrival
-4 hour drink package – Basic Spirits, Premium Beer, Wine and Sparkling til 12AM
-Grazing style canapés and finger food
Early bird and group discounts (10+) available
Purchase your tickets at the bar or through the website
Dress: For Fun and Dancing
Venue information:
• Address: 47 Brambleton Lane St Kilda
• Phone: 6143 2057
• Email: info@quillhouse.com.au
• Website: www.quillhouse.com.au
• Management reserves the right to refuse entry
Images: Images need to be high resolution or vector images so clarity is not lost when the poster is blown up to this size
Poster production:
Poster needs to be created in either Adobe Illustrator or Photoshop so we can easily edit the details if they change after the contest ends
Please provide 3mm internal and external bleed
Theming:
Fun poster with elements of Las Vegas including: dice/casino element, Las Copper Moons, pretty girls, cocktails
25-40 year olds
Casino

```html
<!DOCTYPE html>
<html lang="en">
<head>
<meta charset="utf-8">
<title>Copper Moons – New Years Eve at Quill House</title>
<link rel="stylesheet" href="https://fonts.googleapis.com/css2?family=Russo+One&family=Lobster&family=Audiowide&family=Open+Sans:wght@400;700;800&family=Titan+One&display=swap">
<style>
  :root {
    --gold: #f5c518;
    --gold-deep: #e0a100;
    --yellow: #ffe600;
    --cyan: #3fd8ff;
    --cyan-soft: #8ae9ff;
    --magenta: #ff3fd0;
    --red: #e0182a;
    --blue: #1232c8;
    --ink: #05060c;
    --white: #ffffff;
  }
  * { box-sizing: border-box; margin: 0; padding: 0; }
  html, body { width: 848px; height: 1200px; overflow: hidden; background: var(--ink); }
  .poster {
    position: relative; width: 848px; height: 1200px;
    background: var(--gold); padding: 18px;
    font-family: "Open Sans", Arial, sans-serif;
  }
  .poster__inner { position: relative; width: 100%; height: 100%; background: var(--ink); overflow: hidden; }
  .backdrop {
    position: absolute; inset: 0;
    background:
      radial-gradient(ellipse at 50% 22%, #ffd65a 0%, #d9781a 20%, #6b2a08 42%, transparent 62%),
      linear-gradient(180deg, #2a1406 0%, #120a04 45%, #1a1208 60%, #0a0a10 100%);
  }
  .backdrop__city {
    position: absolute; left: 0; right: 0; top: 640px; bottom: 0;
    background: linear-gradient(180deg, rgba(80,60,30,.2) 0%, #3a2a12 25%, #161018 70%, #090a12 100%);
  }
  .frame {
    position: absolute; left: 20px; top: 18px; width: 774px; height: 1118px;
    border: 6px solid var(--cyan); border-radius: 6px;
    box-shadow: 0 0 14px var(--cyan), inset 0 0 14px var(--cyan);
  }
  .price-badge { position: absolute; left: 42px; top: 14px; width: 240px; height: 240px; }
  .price-badge__wheel {
    position: absolute; inset: 0; border-radius: 50%;
    background: radial-gradient(circle, #6b1010 0%, #2a2a2a 45%, #111 70%, #444 100%);
    border: 6px solid #222;
  }
  .price-badge__amount {
    position: absolute; left: 0; right: 0; top: 78px; text-align: center;
    font-family: "Titan One", sans-serif; font-size: 66px; color: var(--yellow);
    text-shadow: 0 3px 0 var(--gold-deep), 0 0 8px #000;
  }
  .price-badge__note {
    position: absolute; left: 0; right: 0; top: 158px; text-align: center;
    font-family: "Titan One", sans-serif; font-size: 24px; color: var(--yellow);
    text-shadow: 0 2px 3px #000;
  }
  .venue-name {
    position: absolute; left: 440px; top: 52px; width: 340px; text-align: center;
    font-family: "Titan One", sans-serif; font-size: 52px; color: var(--yellow);
  }
  .hours {
    position: absolute; left: 540px; top: 146px;
    font-family: "Russo One", sans-serif; font-size: 27px; color: var(--yellow);
  }
  .date { position: absolute; left: 0; top: 236px; width: 100%; height: 64px; }
  .date__digit {
    position: absolute; top: 0; width: 62px; height: 62px; border-radius: 50%;
    background: radial-gradient(circle, #fff 0 48%, var(--blue) 52%);
    border: 3px solid var(--cyan-soft); box-shadow: 0 0 8px var(--cyan);
    font-family: "Russo One", sans-serif; font-size: 34px; color: var(--red);
    display: flex; align-items: center; justify-content: center;
  }
  .marquee {
    position: absolute; left: 70px; top: 260px; width: 690px; height: 420px;
    background: radial-gradient(ellipse at 50% 42%, #fff6d0 0%, #f4e08a 28%, #c41e1e 44%, #7a0e0e 52%, transparent 66%);
  }
  .event-eyebrow {
    position: absolute; left: 0; right: 0; top: 308px; text-align: center;
    font-family: "Audiowide", sans-serif; font-size: 22px; letter-spacing: 6px; color: var(--red);
  }
  .event-title {
    position: absolute; left: 0; right: 0; top: 340px; text-align: center;
    font-family: "Russo One", sans-serif; font-size: 108px; line-height: 1; color: #c7f4ff;
    -webkit-text-stroke: 3px var(--blue);
    text-shadow: 0 5px 0 #0b1a6b, 0 0 18px var(--cyan);
  }
  .event-title__script {
    position: absolute; left: 0; right: 0; top: 444px; text-align: center;
    font-family: "Lobster", cursive; font-size: 104px; line-height: 1; color: var(--red);
    -webkit-text-stroke: 2px #fff;
    text-shadow: 0 4px 0 #5a0008, 0 0 10px #000;
  }
  .tagline {
    position: absolute; left: 0; right: 0; top: 586px; text-align: center;
    font-family: "Audiowide", sans-serif; font-size: 42px; line-height: 52px; color: var(--yellow);
    text-transform: uppercase; text-shadow: 0 3px 0 #6a3a00, 0 0 6px #000;
  }
  .details {
    position: absolute; left: 0; right: 0; top: 770px; text-align: center;
    text-transform: uppercase; font-weight: 700;
  }
  .details__line { font-size: 18px; line-height: 26px; }
  .details__line--pink { color: #ff4fd8; }
  .details__line--white { color: var(--white); }
  .details__line--light { color: #ff6fe0; font-weight: 400; }
  .details__line--small { font-size: 13px; color: var(--white); line-height: 22px; }
  .offer {
    position: absolute; left: 0; right: 0; top: 906px; text-align: center;
    font-family: "Audiowide", sans-serif; font-size: 18px; line-height: 24px; color: var(--yellow);
    text-transform: uppercase;
  }
  .contact {
    position: absolute; left: 0; right: 0; top: 956px; text-align: center;
    text-transform: uppercase; color: var(--cyan-soft); font-weight: 800;
  }
  .contact__heading { font-size: 11px; color: var(--white); line-height: 20px; }
  .contact__item { font-size: 21px; line-height: 26px; }
  .contact__item::before { content: "•"; margin-right: 22px; }
  .contact__fine { font-size: 11px; color: var(--white); line-height: 18px; }
  .contact__fine::before { content: "•"; margin-right: 22px; }
</style>
</head>
<body>
<main class="poster">
  <div class="poster__inner">
    <div class="backdrop" role="img" aria-label="Fireworks bursting in gold and magenta over dark sunburst rays"></div>
    <div class="backdrop__city" role="img" aria-label="Night view of a glittering city strip with casino towers"></div>
    <div class="frame"></div>

    <div class="price-badge">
      <div class="price-badge__wheel" role="img" aria-label="Roulette wheel"></div>
      <div class="price-badge__amount">$105</div>
      <div class="price-badge__note">ALL INCLUSIVE</div>
    </div>

    <div class="venue-name">Quill House</div>
    <div class="hours">8PM-3AM</div>

    <div class="marquee" role="img" aria-label="Illuminated casino marquee sign with dice, playing card suits, poker chips and a golden ribbon banner"></div>

    <div class="date" aria-label="31.12.12">
      <span class="date__digit" style="left:134px">3</span>
      <span class="date__digit" style="left:213px">1</span>
      <span class="date__digit" style="left:316px">1</span>
      <span class="date__digit" style="left:398px">2</span>
      <span class="date__digit" style="left:518px">1</span>
      <span class="date__digit" style="left:603px">2</span>
    </div>

    <div class="event-eyebrow">NEW YEARS EVE</div>
    <h1 class="event-title">COPPER</h1>
    <div class="event-title__script">Moons</div>

    <p class="tagline">What happens at Quill<br>stays at Quill</p>

    <section class="details">
      <p class="details__line details__line--pink">Includes a cocktail on arrival</p>
      <p class="details__line details__line--white">4 hour drink package</p>
      <p class="details__line details__line--light">Basic spirits, premium beer, wine and sparkling til 12AM</p>
      <p class="details__line details__line--pink">Grazing style canapés and finger food</p>
      <p class="details__line--small">Dress: for fun and dancing</p>
    </section>

    <section class="offer">
      <p>Early bird and group discounts (10+) available</p>
      <p>Purchase your tickets at the bar or through the website</p>
    </section>

    <section class="contact">
      <p class="contact__heading">Venue information:</p>
      <p class="contact__item">Address: 47 Brambleton Lane St Kilda</p>
      <p class="contact__item">Phone: 6143 2057</p>
      <p class="contact__item">Email: info@quillhouse.com.au</p>
      <p class="contact__item">Website: www.quillhouse.com.au</p>
      <p class="contact__fine">Management reserves the right to refuse entry</p>
    </section>
  </div>
</main>
</body>
</html>
```